Design & Content Treatments for small Tai Chi Teacher's Site

Wordpress is setup and ready to go. Really just need a header image (with text treatment of the site name and tag line), and really simple content treatments for each page (image selection and placement, etc). Ideally this will require very little modification to the actual wordpress template code.
Simpler is better. I will post images and am in the process of flowing all the text into the site now. If some sort of Iconic identity can be established Marek will be VERY happy, but it's not a requirement
Thank You!
Temporary Site URL is http://203.0.113.58/~cedarlx4/
Final will be cedarlanternmovement.com.

```html
<!DOCTYPE html>
<html lang="en">
<head>
<meta charset="utf-8">
<title>Cedar Lantern Movement — Blog</title>
<link rel="stylesheet" href="https://fonts.googleapis.com/css2?family=Arimo:wght@400&family=Raleway:wght@300&family=Ubuntu:wght@400&display=swap">
<style>
:root{
  --bg-top:#cdc6bd;
  --bg-bottom:#dedad4;
  --paper:#ffffff;
  --side:#efebe6;
  --nav-top:#5d5650;
  --nav-bottom:#37312d;
  --nav-sep:#6c655f;
  --ink:#222222;
  --body:#7a7672;
  --link:#9a7a5a;
  --meta-bg:#3e3935;
  --frame:#ebe7e2;
  --photo-a:#d99c66;
  --photo-b:#8a5a3a;
  --rule:#b9b3ab;
  --pill:#7b736c;
  --icon:#8a8078;
}
*{box-sizing:border-box;margin:0;padding:0}
html,body{width:1058px;height:1200px;overflow:hidden}
body{
  background:linear-gradient(to bottom,var(--bg-top) 0,var(--bg-top) 396px,var(--bg-bottom) 396px);
  font-family:Arimo,Arial,sans-serif;color:var(--body);position:relative;
}
.page{position:absolute;left:67px;top:26px;width:927px;height:1114px;background:var(--paper);overflow:hidden}
.site-name{position:absolute;left:30px;top:30px;font-family:Raleway,sans-serif;font-weight:300;font-size:36px;color:#2d2a27;letter-spacing:-0.5px}
.search{position:absolute;left:721px;top:37px;width:190px;height:27px;border:1px solid #dcd7d1;background:#f6f4f1;font-size:12px;color:#999;padding:6px 8px}
.search svg{position:absolute;right:8px;top:6px}
.nav{position:absolute;left:10px;top:106px;width:906px;height:46px;background:linear-gradient(var(--nav-top),var(--nav-bottom));display:flex;font-family:Ubuntu,sans-serif;font-size:13px;color:#fff}
.nav a{color:#fff;text-decoration:none;display:flex;align-items:center;justify-content:center;border-right:1px solid var(--nav-sep);height:100%}
.nav a:last-child{border-right:0}
.sidebar{position:absolute;left:646px;top:152px;width:270px;height:912px;background:var(--side);padding:24px 18px}
.sidebar h2{font-weight:400;font-size:23px;color:var(--ink);margin-bottom:12px}
.cats{list-style:none;font-size:12px;color:#666;width:232px;margin-bottom:54px}
.cats li{height:24px;line-height:22px;border-bottom:1px dotted #a49d95}
.cats li.muted{color:#aaa}
.pill{display:inline-block;background:var(--pill);color:#fff;font-size:11px;border-radius:9px;padding:2px 10px}
.cal{width:235px;border-collapse:collapse;font-size:12px;color:#666;margin:6px 0 6px;text-align:center}
.cal th{font-weight:400;height:22px;border-bottom:1px solid #cfc9c1}
.cal td{height:18.5px}
.posts{position:absolute;left:10px;top:182px;width:630px}
.post{position:relative;height:212.5px}
.thumb{position:absolute;left:0;top:0;width:172px;height:192px;background:var(--frame);padding:6px}
.thumb div{width:100%;height:100%;background:linear-gradient(120deg,var(--photo-a),#c98652 55%,var(--photo-b))}
.thumb.faded div{opacity:.45}
.zoom{position:absolute;left:52px;top:62px}
.post h3{position:absolute;left:185px;top:0;font-weight:400;font-size:23px;color:var(--ink);white-space:nowrap}
.meta{position:absolute;left:187px;top:33px;background:var(--meta-bg);color:#fff;font-size:10.5px;padding:3px 5px;white-space:nowrap}
.post p{position:absolute;left:186px;top:62px;width:430px;font-size:11.6px;line-height:14px}
.more{position:absolute;left:184px;top:166px;font-size:12px;color:var(--link)}
.footer-rule{position:absolute;left:10px;top:1066px;width:906px;border-top:1px dotted var(--rule)}
.copy{position:absolute;left:15px;top:1084px;font-size:12px;color:#555}
.social{position:absolute;left:835px;top:1080px;display:flex;gap:6px}
.social span{width:23px;height:23px;border-radius:3px;background:var(--icon)}
</style>
</head>
<body>
<div class="page">
  <div class="site-name">Cedar Lantern Movement</div>
  <div class="search">Search
    <svg width="14" height="14" viewBox="0 0 14 14"><circle cx="6" cy="6" r="4.5" fill="none" stroke="#aaa" stroke-width="1.8"/><line x1="9.3" y1="9.3" x2="13" y2="13" stroke="#aaa" stroke-width="2"/></svg>
  </div>
  <nav class="nav">
    <a style="width:91px">Home</a>
    <a style="width:126px">Class Schedule</a>
    <a style="width:150px">About T’ai Chi Ch’uan</a>
    <a style="width:297px">Mentorship and Constructive Life Guidance</a>
    <a style="width:136px">Contact Marek</a>
    <a style="width:106px">Blog</a>
  </nav>

  <div class="posts">
    <article class="post">
      <div class="thumb faded"><div role="img" aria-label="Photo of a teacher practising a staff form in a studio"></div></div>
      <svg class="zoom" width="68" height="68" viewBox="0 0 68 68"><circle cx="34" cy="34" r="31" fill="none" stroke="#fff" stroke-width="3"/><circle cx="31" cy="31" r="9" fill="none" stroke="#fff" stroke-width="4"/><line x1="38" y1="38" x2="45" y2="45" stroke="#fff" stroke-width="5" stroke-linecap="round"/></svg>
      <h3>Lorem ipsum dolor sit amet</h3>
      <span class="meta">Dana Kell on Apr 21st 2011 with 14 comments</span>
      <p>Lorem ipsum dolor sit amet, consectetuer adipiscing elit, sed diam nonummy nibh euismod tincidunt ut laoreet dolore magna aliquam erat volutpat. Ut wisi enim ad minim veniam, quis nostrud exerci tation ullamcorper suscipit lobortis nisl ut aliquip ex ea commodo consequat. Duis autem vel eum iriure dolor in hendrerit in vulputate velit esse molestie consequat, vel illum dolore eu feugiat nulla facilisis at vero eros et accumsan et iusto odio dignissim qui blandit praesent luptatum zzril delenit augue duis dolore te feugait nulla facilisi.</p>
      <span class="more">Readmore »</span>
    </article>
    <article class="post">
      <div class="thumb"><div role="img" aria-label="Photo of a teacher practising a staff form in a studio"></div></div>
      <h3>Lorem ipsum dolor sit amet</h3>
      <span class="meta">Dana Kell on Apr 21st 2011 with 14 comments</span>
      <p>Lorem ipsum dolor sit amet, consectetuer adipiscing elit, sed diam nonummy nibh euismod tincidunt ut laoreet dolore magna aliquam erat volutpat. Ut wisi enim ad minim veniam, quis nostrud exerci tation ullamcorper suscipit lobortis nisl ut aliquip ex ea commodo consequat. Duis autem vel eum iriure dolor in hendrerit in vulputate velit esse molestie consequat, vel illum dolore eu feugiat nulla facilisis at vero eros et accumsan et iusto odio dignissim qui blandit praesent luptatum zzril delenit augue duis dolore te feugait nulla facilisi.</p>
      <span class="more">Readmore »</span>
    </article>
    <article class="post">
      <div class="thumb"><div role="img" aria-label="Photo of a teacher practising a staff form in a studio"></div></div>
      <h3>Lorem ipsum dolor sit amet</h3>
      <span class="meta">Dana Kell on Apr 21st 2011 with 14 comments</span>
      <p>Lorem ipsum dolor sit amet, consectetuer adipiscing elit, sed diam nonummy nibh euismod tincidunt ut laoreet dolore magna aliquam erat volutpat. Ut wisi enim ad minim veniam, quis nostrud exerci tation ullamcorper suscipit lobortis nisl ut aliquip ex ea commodo consequat. Duis autem vel eum iriure dolor in hendrerit in vulputate velit esse molestie consequat, vel illum dolore eu feugiat nulla facilisis at vero eros et accumsan et iusto odio dignissim qui blandit praesent luptatum zzril delenit augue duis dolore te feugait nulla facilisi.</p>
      <span class="more">Readmore »</span>
    </article>
    <article class="post">
      <div class="thumb"><div role="img" aria-label="Photo of a teacher practising a staff form in a studio"></div></div>
      <h3>Lorem ipsum dolor sit amet</h3>
      <span class="meta">Dana Kell on Apr 21st 2011 with 14 comments</span>
      <p>Lorem ipsum dolor sit amet, consectetuer adipiscing elit, sed diam nonummy nibh euismod tincidunt ut laoreet dolore magna aliquam erat volutpat. Ut wisi enim ad minim veniam, quis nostrud exerci tation ullamcorper suscipit lobortis nisl ut aliquip ex ea commodo consequat. Duis autem vel eum iriure dolor in hendrerit in vulputate velit esse molestie consequat, vel illum dolore eu feugiat nulla facilisis at vero eros et accumsan et iusto odio dignissim qui blandit praesent luptatum zzril delenit augue duis dolore te feugait nulla facilisi.</p>
      <span class="more">Readmore »</span>
    </article>
  </div>

  <aside class="sidebar">
    <h2>Category</h2>
    <ul class="cats">
      <li>Category post one</li>
      <li class="muted">Category post two</li>
      <li>Category post three</li>
      <li>Category post four</li>
      <li>Category post five</li>
    </ul>
    <h2>Upcoming Classes</h2>
    <span class="pill">April 2011</span>
    <table class="cal">
      <tr><th>S</th><th>M</th><th>T</th><th>W</th><th>T</th><th>F</th><th>S</th></tr>
      <tr><td></td><td></td><td></td><td></td><td></td><td>1</td><td>2</td></tr>
      <tr><td>3</td><td>4</td><td>5</td><td>6</td><td>7</td><td>8</td><td>9</td></tr>
      <tr><td>10</td><td>11</td><td>12</td><td>13</td><td>14</td><td>15</td><td>16</td></tr>
      <tr><td>17</td><td>18</td><td>19</td><td>20</td><td>21</td><td>22</td><td>23</td></tr>
      <tr><td>24</td><td>25</td><td>26</td><td>27</td><td>28</td><td>29</td><td>30</td></tr>
    </table>
    <span class="pill">« Mar</span>
  </aside>

  <div class="footer-rule"></div>
  <div class="copy">© 2011 - Cedar Lantern Movement</div>
  <div class="social"><span aria-label="Social link"></span><span aria-label="Social link"></span><span aria-label="Feed link"></span></div>
</div>
</body>
</html>
```